Clean Energy Brand - Business Card and Letterhead Designs

Hi, everyone! We need a graphic designer who has experience working with the energy sector. We want help designing a perfect two-sided business card and letterhead for a clean energy company we've been assisting. We have a great new logo and all of the associated files.Our client is looking for a design that is "disruptive," "future-facing," "masculine," "bold," and "empowering." The colours of the logo are navy blue and orange and are meant to stand out. We'll need all ownership and copyright paperwork as well as first proofs in a 48-hour period.

Target Market(s)

Government; Non-Profits; Clean Energy Industry; Municipalities; North American Energy Sector

Industry/Entity Type

Power Generation

Requirements
Must have
• A matching business card and letterhead design
Should not have
• Must not be from a template

```html
<!DOCTYPE html>
<html lang="en">
<head>
<meta charset="utf-8">
<title>Northwind Clean Energy – Letterhead</title>
<link rel="stylesheet" href="https://fonts.googleapis.com/css2?family=Arimo:wght@400;700&display=swap">
<style>
  :root {
    --navy: #1b2a5c;
    --orange: #f26a2e;
    --text-grey: #6f7072;
    --light-grey: #a7a9ac;
    --backdrop: #dfe2e3;
    --paper: #ffffff;
    --signature-tone: #e4e5e6;
  }
  * { box-sizing: border-box; margin: 0; padding: 0; }
  html, body { width: 1200px; height: 784px; overflow: hidden; }
  body {
    background: var(--backdrop);
    font-family: "Arimo", Arial, sans-serif;
    display: flex;
    align-items: center;
    justify-content: center;
  }
  .letterhead {
    position: relative;
    width: 520px;
    height: 736px;
    background: var(--paper);
    border-top: 5px solid var(--orange);
    box-shadow: 0 2px 10px rgba(0,0,0,0.12);
    padding: 48px 46px 0 64px;
  }
  .brand {
    display: flex;
    align-items: center;
    justify-content: flex-end;
    gap: 10px;
    margin-bottom: 40px;
  }
  .brand-name {
    color: var(--navy);
    font-weight: 700;
    font-size: 22px;
    letter-spacing: 0.2px;
  }
  .brand-dot {
    width: 22px; height: 22px;
    border-radius: 50%;
    background: var(--orange);
  }
  .letter-body {
    color: var(--text-grey);
    font-size: 9.6px;
    line-height: 1.45;
    margin-left: 60px;
  }
  .letter-body p { margin-bottom: 14px; }
  .signature {
    width: 150px;
    height: 46px;
    margin: 26px 0 0 0;
    background: var(--signature-tone);
    border-radius: 3px;
  }
  .footer {
    position: absolute;
    left: 64px;
    right: 46px;
    bottom: 44px;
  }
  .footer-rule {
    display: flex;
    align-items: center;
    gap: 10px;
    margin-bottom: 8px;
  }
  .footer-rule .line { flex: 0 0 44px; height: 1px; background: var(--light-grey); }
  .contact-icons { display: flex; gap: 8px; }
  .contact-icons svg { width: 14px; height: 14px; display: block; }
  .address {
    color: var(--navy);
    font-weight: 700;
    font-size: 9px;
    margin-bottom: 5px;
  }
  .contact-line {
    display: flex;
    gap: 8px;
    color: var(--text-grey);
    font-size: 8.5px;
  }
  .contact-line .sep { width: 1px; background: var(--orange); }
</style>
</head>
<body>
  <main class="letterhead">
    <header class="brand">
      <span class="brand-dot"></span>
      <span class="brand-name">Northwind Clean Energy</span>
    </header>

    <section class="letter-body">
      <p>Lorem Ipsum is simply dummy text of the printing and typesetting industry. Lorem Ipsum has been the industry's standard dummy text ever since the 1500s, when an unknown printer took a galley of type and scrambled it to make a type specimen book. It has survived not only five centuries, but also the leap into electronic typesetting, remaining essentially unchanged. It was popularised in the 1960s with the release of transfer sheets containing Lorem Ipsum passages, and more recently with desktop publishing software and layout programs including versions of Lorem Ipsum.</p>
      <p>It is a long established fact that a reader will be distracted by the readable content of a page when looking at its layout. The point of using Lorem Ipsum is that it has a more-or-less normal distribution of letters, as opposed to using 'Content here, content here', making it look like readable English. Many desktop publishing packages and web page editors now use Lorem Ipsum as their default model text, and a search for 'lorem ipsum' will uncover many web sites still in their infancy. Various versions have evolved over the years, sometimes by accident, sometimes on purpose (injected humour and the like).</p>
      <p>Contrary to popular belief, Lorem Ipsum is not simply random text. It has roots in a piece of classical Latin literature from 45 BC, making it over 2000 years old. A retired teacher at a small coastal school looked up one of the more obscure Latin words, consectetur, from a Lorem Ipsum passage, and going through the cites of the word in classical literature, discovered the undoubtable source. Lorem Ipsum comes from sections 1.10.32 and 1.10.33 of an old treatise on ethics, combined with a handful of model sentence structures, to generate Lorem Ipsum which looks reasonable. The generated Lorem Ipsum is therefore always free from repetition, injected humour, or non-characteristic words etc.</p>
    </section>

    <div class="signature" role="img" aria-label="Handwritten signature of the sender"></div>

    <footer class="footer">
      <div class="footer-rule">
        <span class="line"></span>
        <div class="contact-icons">
          <svg viewBox="0 0 14 14" aria-label="Address"><circle cx="7" cy="7" r="7" fill="var(--orange)"/><path d="M7 3.2a2.4 2.4 0 0 0-2.4 2.4C4.6 7.6 7 10.8 7 10.8s2.4-3.2 2.4-5.2A2.4 2.4 0 0 0 7 3.2z" fill="#fff"/><circle cx="7" cy="5.6" r="0.9" fill="var(--orange)"/></svg>
          <svg viewBox="0 0 14 14" aria-label="Phone"><circle cx="7" cy="7" r="7" fill="var(--orange)"/><path d="M5 3.6l1 1.8-0.7 0.8c0.4 0.9 1.1 1.6 2 2l0.8-0.7 1.8 1-0.5 1.4c-2.8 0-5-2.2-5-5z" fill="#fff"/></svg>
          <svg viewBox="0 0 14 14" aria-label="Email"><circle cx="7" cy="7" r="7" fill="var(--orange)"/><rect x="3.6" y="4.6" width="6.8" height="4.8" fill="#fff"/><path d="M3.6 4.6L7 7.3l3.4-2.7" fill="none" stroke="var(--orange)" stroke-width="0.7"/></svg>
          <svg viewBox="0 0 14 14" aria-label="Website"><circle cx="7" cy="7" r="7" fill="var(--orange)"/><circle cx="7" cy="7" r="3.6" fill="none" stroke="#fff" stroke-width="0.8"/><path d="M3.4 7h7.2M7 3.4c-1.6 2-1.6 5.2 0 7.2M7 3.4c1.6 2 1.6 5.2 0 7.2" fill="none" stroke="#fff" stroke-width="0.7"/></svg>
        </div>
        <span class="line"></span>
      </div>
      <p class="address">00 Sample Ridge Road, CA 0000</p>
      <p class="contact-line">
        <span>00 000 0000</span><span class="sep"></span>
        <span>contact@northwindcleanenergy.ca</span><span class="sep"></span>
        <span>www.northwindcleanenergy.ca</span>
      </p>
    </footer>
  </main>
</body>
</html>
```